Instant Broth for Ramen and Soup - Need labels for three flavors

We are a new company planning to launch a line of all natural powdered instant broth for ramen and soups. We need a logo design for our three launch flavors which will be Chicken, Prime Beef and Garden Vegetable. The powdered broth will be sold in 4oz containers with a white cap.
We would like the logo to be at the top of the label and or product description "Instant Broth for Ramen and Soups" underneath. The product description should stand out to the consumer, so it should likely be a larger font and one that compliments the logo. Below the Product description, we would like the name of the flavor and appropriate color scheme to match the flavor (see product picture for color). The design for each flavor should be the same, the only thing that should change is the color scheme to match flavor. Because we use all natural ingredients we would also like the label to state "Natural Ingredients" and "Gluten Free" on the front.
Additionally if you could please include placeholders for the nutritional label, ingredients list beneath, net size/weight on the side, bar code and a placeholder address for "Veltmore Foods LLC" that would be great as we are still finalizing these details. We would also like the label design to be catchy and interesting while complimenting the fun light-hearted logo.
Lastly, if your design is chosen you will be our main choice for additional design work (if you wish) including, top label design for the cap, finalizing the product info, formatting actual jar dimensions and other design work for the many other additional flavors we will be releasing.
Target Market(s)
Homemade ramen and soup connoisseurs, health conscious consumers, millennials and college students
Industry/Entity Type
It Company
Other font styles liked:
- SingleSleeve
Colors
Designer to choose colors to be used in the design.
Requirements
Must have
- 1) Logo
- 2) Product description "Instant Broth for Ramen and Soups"
- 3) Flavor title and color scheme
- 4) "Natural Ingredients" and "Gluten Free"
- 5) Place holder info for FDA required information (nutrition facts, net weight etc.)
Nice to have
- 1) Instructions (placeholder)
- 2) Additional info about the product (placeholder)

```html
<!DOCTYPE html>
<html lang="en">
<head>
<meta charset="utf-8">
<title>Brothwell Instant Broth Labels</title>
<link rel="stylesheet" href="https://fonts.googleapis.com/css2?family=Bubblegum+Sans&family=Nunito:wght@700&display=swap">
<style>
  :root {
    --backdrop: #c9c9c9;
    --paper: #ffffff;
    --title-green: #3b8a2f;
    --bowl-green: #3d8a31;
    --ink: #3a3a3a;
    --chicken: #dfc415;
    --beef: #7d6125;
    --veggie: #c47a27;
  }
  * { margin: 0; padding: 0; box-sizing: border-box; }
  html, body { width: 1200px; height: 983px; overflow: hidden; background: var(--backdrop); }
  .board { position: relative; width: 1200px; height: 983px; }

  .label {
    position: absolute; width: 454px; height: 392px;
    background: var(--paper); overflow: hidden;
  }
  .label--chicken { left: 69px; top: 68px; --accent: var(--chicken); }
  .label--beef { left: 676px; top: 68px; --accent: var(--beef); }
  .label--veggie { left: 369px; top: 522px; --accent: var(--veggie); }

  .band { position: absolute; left: 0; width: 100%; background: var(--accent); }
  .band--top { top: 0; height: 24px; }
  .band--bottom { bottom: 0; height: 25px; }

  .brand {
    position: absolute; top: 40px; width: 100%; text-align: center;
    font-family: "Bubblegum Sans", cursive; font-size: 27px; color: #1d1d1d;
    letter-spacing: 1px; line-height: 1;
  }
  .title {
    position: absolute; width: 100%; text-align: center;
    font-family: "Bubblegum Sans", cursive; color: var(--title-green); line-height: 1;
  }
  .title--top { top: 86px; font-size: 49px; }
  .title--bottom { top: 166px; font-size: 49px; }
  .connector {
    position: absolute; top: 136px; left: 0; width: 100%;
    display: flex; justify-content: center; align-items: center; gap: 10px;
    font-family: "Bubblegum Sans", cursive; font-size: 31px; color: var(--ink); line-height: 1;
  }
  .connector .rule { width: 98px; height: 2px; background: var(--accent); }

  .claim {
    position: absolute; left: 37px; top: 232px; width: 100px; height: 80px;
  }
  .claim svg { position: absolute; inset: 0; }
  .claim-text {
    position: absolute; left: 4px; top: 13px; width: 84px; text-align: center;
    font-family: "Nunito", sans-serif; font-weight: 700; font-size: 11.5px;
    line-height: 1.1; color: #fff;
  }
  .claim-text span { display: block; margin-top: 10px; }

  .art {
    position: absolute; left: 130px; top: 222px; width: 260px; height: 170px;
    border-radius: 70px 70px 40px 40px;
    background: linear-gradient(180deg, var(--accent) 0%, var(--accent) 45%, var(--bowl-green) 62%, var(--bowl-green) 100%);
  }
  .flavor {
    position: absolute; left: 130px; width: 260px; text-align: center;
    font-family: "Bubblegum Sans", cursive; color: #fff; line-height: 0.95;
  }
  .flavor--single { top: 260px; font-size: 48px; transform: rotate(-6deg); }
  .flavor--double { top: 252px; font-size: 34px; transform: rotate(6deg); }
</style>
</head>
<body>
<main class="board">

  <section class="label label--chicken">
    <div class="band band--top"></div>
    <div class="brand">Brothwell</div>
    <h1 class="title title--top">Instant Broth</h1>
    <div class="connector"><span class="rule"></span>for<span class="rule"></span></div>
    <h2 class="title title--bottom">Ramen and Soups</h2>
    <div class="art" role="img" aria-label="Illustration of a roast chicken in a green soup bowl with scattered herbs"></div>
    <div class="flavor flavor--single">chicken</div>
    <div class="claim">
      <svg viewBox="0 0 100 80" aria-hidden="true"><path d="M46 2C20 2 2 17 2 38s18 36 44 36c9 0 16-2 22-5l28 8-18-16c4-6 6-14 6-23C84 17 72 2 46 2z" fill="var(--accent)"/></svg>
      <p class="claim-text">Natural Ingredients<span>Gluten Free</span></p>
    </div>
    <div class="band band--bottom"></div>
  </section>

  <section class="label label--beef">
    <div class="band band--top"></div>
    <div class="brand">Brothwell</div>
    <h1 class="title title--top">Instant Broth</h1>
    <div class="connector"><span class="rule"></span>for<span class="rule"></span></div>
    <h2 class="title title--bottom">Ramen and Soups</h2>
    <div class="art" role="img" aria-label="Illustration of a beef steak in a green soup bowl with scattered herbs"></div>
    <div class="flavor flavor--single">beef</div>
    <div class="claim">
      <svg viewBox="0 0 100 80" aria-hidden="true"><path d="M46 2C20 2 2 17 2 38s18 36 44 36c9 0 16-2 22-5l28 8-18-16c4-6 6-14 6-23C84 17 72 2 46 2z" fill="var(--accent)"/></svg>
      <p class="claim-text">Natural Ingredients<span>Gluten Free</span></p>
    </div>
    <div class="band band--bottom"></div>
  </section>

  <section class="label label--veggie">
    <div class="band band--top"></div>
    <div class="brand">Brothwell</div>
    <h1 class="title title--top">Instant Broth</h1>
    <div class="connector"><span class="rule"></span>for<span class="rule"></span></div>
    <h2 class="title title--bottom">Ramen and Soups</h2>
    <div class="art" role="img" aria-label="Illustration of a pumpkin in a green soup bowl with scattered herbs"></div>
    <div class="flavor flavor--double">Garden<br>Vegetables</div>
    <div class="claim">
      <svg viewBox="0 0 100 80" aria-hidden="true"><path d="M46 2C20 2 2 17 2 38s18 36 44 36c9 0 16-2 22-5l28 8-18-16c4-6 6-14 6-23C84 17 72 2 46 2z" fill="var(--accent)"/></svg>
      <p class="claim-text">Natural Ingredients<span>Gluten Free</span></p>
    </div>
    <div class="band band--bottom"></div>
  </section>

</main>
</body>
</html>
```